Need a book cover design for a Lumora Book on Herbal Remedies

I need a book cover for my new ebook, here are the details:
Title: Meadow Cures
Sub-Heading: Buried Ancient Garden Tonics
Reclaiming the Wisdom of Roots for Everyday Wellness and Strength
Author: Nora Belcourt

```html
<!DOCTYPE html>
<html lang="en">
<head>
<meta charset="utf-8">
<title>Meadow Cures — Nora Belcourt</title>
<link rel="stylesheet" href="https://fonts.googleapis.com/css2?family=Amatic+SC:wght@400;700&display=swap">
<style>
  :root {
    --backdrop: #bcc0d6;
    --paper: #ffffff;
    --leaf-light: #8fd3ad;
    --leaf-mid: #4fb48a;
    --leaf-deep: #1f7f6a;
    --title-teal: #1d7d74;
    --title-green: #4e9e5e;
    --subtitle-ink: #1a6b63;
    --tagline-gold: #b48a3c;
    --author-ink: #2a6e4a;
  }
  * { margin: 0; padding: 0; box-sizing: border-box; }
  html, body {
    width: 1200px;
    height: 2952px;
    overflow: hidden;
    background: var(--backdrop);
  }
  .canvas {
    position: relative;
    width: 1200px;
    height: 2952px;
  }
  .book-cover {
    position: absolute;
    left: 80px;
    top: 646px;
    width: 1040px;
    height: 1660px;
    background: var(--paper);
    overflow: hidden;
    box-shadow: 0 6px 24px rgba(60, 66, 100, 0.18);
  }
  .foliage-frame {
    position: absolute;
    inset: 0;
    background:
      radial-gradient(ellipse 62% 62% at 50% 52%, rgba(255,255,255,0) 62%, rgba(143,211,173,0.55) 82%, rgba(79,180,138,0.85) 100%),
      linear-gradient(180deg, rgba(79,180,138,0.55) 0%, rgba(255,255,255,0) 12%, rgba(255,255,255,0) 88%, rgba(79,180,138,0.6) 100%);
  }
  .cover-text {
    position: absolute;
    inset: 0;
    text-align: center;
    font-family: "Amatic SC", cursive;
  }
  .tagline {
    position: absolute;
    top: 262px;
    left: 0; right: 0;
    font-size: 56px;
    font-weight: 400;
    letter-spacing: 5px;
    line-height: 1.05;
    color: var(--tagline-gold);
  }
  .title {
    position: absolute;
    top: 440px;
    left: 0; right: 0;
    font-weight: 700;
    font-size: 270px;
    line-height: 0.82;
    letter-spacing: 2px;
  }
  .title-line { display: block; }
  .title-line--first { color: var(--title-teal); }
  .title-line--second { color: var(--title-green); }
  .subtitle {
    position: absolute;
    top: 982px;
    left: 170px; right: 170px;
    font-size: 72px;
    font-weight: 700;
    line-height: 1.0;
    color: var(--subtitle-ink);
  }
  .author {
    position: absolute;
    top: 1378px;
    left: 0; right: 0;
    font-size: 78px;
    font-weight: 700;
    letter-spacing: 8px;
    color: var(--author-ink);
  }
</style>
</head>
<body>
<main class="canvas">
  <section class="book-cover">
    <div class="foliage-frame" role="img" aria-label="Watercolour border of green leaves and fine gold sprigs framing the cover"></div>
    <div class="cover-text">
      <p class="tagline">Buried Ancient Garden<br>Tonics</p>
      <h1 class="title">
        <span class="title-line title-line--first">Meadow</span>
        <span class="title-line title-line--second">Cures</span>
      </h1>
      <p class="subtitle">Reclaiming the Wisdom of Roots for Everyday Wellness and Strength</p>
      <p class="author">Nora Belcourt</p>
    </div>
  </section>
</main>
</body>
</html>
```